Recipe mobile app, new flow and design for uploading recipe process

I need a new recipe upload process that's simple, intuitive, and engaging.
The goal is to have a user-friendly and fast flow.
The app is a social recipe library where anyone can upload a recipe after signing up. I currently have a flow, but it's "boring," so I'd like to significantly improve this aspect of the app.
When I create a new recipe, it's immediately saved and labeled as a draft. I'll then need to specify:
- Recipe title
- Cover image (required)
- Number of people (how many people is the recipe for)
- Ingredients (name, quantity, and unit of measurement)
- Recipe explanation (broken down into steps, and I can optionally attach an image to each step)
- Upload
Every change is immediately saved, so you can edit, exit, and resume editing later.
I've attached images of the app and the current upload process.
Thank you.
Low design quality
Good morning everyone,
some of the designs received are fantastic, but please make sure to carefully read the requirement so as not to do extra work.
The requirement is to redesign the flow that a user follows when uploading a recipe to the platform.
We have uploaded the current app screens to give you an idea of what the product looks like, what the colors and style are, but we don’t need a full redesign - only the part mentioned above, while keeping the existing style and colors (we cannot rework the entire theme).
To clarify: if you look at the screens shared in the zip file attached to the project, the focus should be on the screens from 5_.png to 10_.png.
These screens can be redesigned in the most creative way you think, as long as the overall theme remains unchanged.
Thank you for your attention.

```html
<!DOCTYPE html>
<html lang="en">
<head>
<meta charset="utf-8">
<title>New Recipe Flow</title>
<link href="https://fonts.googleapis.com/css2?family=Poppins:wght@400;500;600;700&display=swap" rel="stylesheet">
<style>
:root{
  --orange:#E98D56;
  --orange-strong:#E5823E;
  --orange-text:#E06B2A;
  --teal:#1AA899;
  --green:#1FA65A;
  --ink:#2E2E2E;
  --muted:#8A8A8A;
  --line:#E4E4E4;
  --panel:#F2F2F2;
  --bg:#FFFFFF;
  --red:#E0473A;
}
*{box-sizing:border-box;margin:0;padding:0}
html,body{width:682px;height:1200px;overflow:hidden;background:var(--bg)}
body{position:relative;font-family:'Poppins',sans-serif;color:var(--ink)}
.flow-label{position:absolute;writing-mode:vertical-rl;transform:rotate(180deg);color:var(--orange-text);font-size:9px;font-weight:500;letter-spacing:5px;white-space:nowrap}
.screen{position:absolute;width:260px;height:540px;border-radius:30px;overflow:hidden;background:#fff;box-shadow:0 0 0 5px #1b1b1b}
.header{position:absolute;left:0;top:0;width:100%;height:130px;background:var(--orange)}
.status{position:absolute;top:14px;left:26px;right:24px;display:flex;justify-content:space-between;align-items:center;color:#fff;font-size:10px;font-weight:600}
.titlebar{position:absolute;top:42px;left:18px;right:18px;display:flex;justify-content:space-between;align-items:center;color:#fff}
.titlebar h1{font-size:11.5px;font-weight:600}
.body{position:absolute;top:117px;left:0;right:0;bottom:0;background:#fff;border-radius:14px 14px 0 0}
.step-badge{position:absolute;left:50%;top:-22px;transform:translateX(-50%);width:54px;height:54px}
.step-meta{position:absolute;top:48px;width:100%;text-align:center}
.step-meta small{display:block;font-size:7px;color:var(--muted);letter-spacing:.3px}
.step-meta strong{display:block;font-size:9px;font-weight:600;margin-top:3px}
.label{position:absolute;left:14px;font-size:7px;font-weight:500}
.footer{position:absolute;left:14px;right:14px;top:340px}
.progress-row{display:flex;justify-content:space-between;font-size:5.5px;line-height:8px;font-weight:600;color:#555}
.bar{margin-top:4px;height:4px;border-radius:2px;background:var(--line)}
.bar i{display:block;height:100%;border-radius:2px;background:var(--green)}
.buttons{display:flex;gap:12px;margin-top:12px}
.btn{flex:1;height:24px;border-radius:12px;display:flex;align-items:center;justify-content:center;gap:5px;font-size:8.5px;font-weight:600}
.btn-next{background:var(--orange-strong);color:#fff}
.btn-prev{border:1px solid var(--orange-strong);color:var(--orange-strong)}
.home{position:absolute;bottom:10px;left:50%;transform:translateX(-50%);width:96px;height:3px;border-radius:2px;background:#1b1b1b}
.name-field{position:absolute;left:14px;right:14px;top:110px;padding-bottom:7px;border-bottom:1px solid var(--line);text-align:center;font-size:11px;font-weight:600;color:#777}
.photo-box{position:absolute;left:14px;right:14px;top:166px;height:140px;border:1px dashed #E6C9B6;border-radius:4px}
.illustration{position:absolute;left:76px;top:16px;width:78px;height:78px;border-radius:50%;background:radial-gradient(circle at 45% 45%,#F2A25A,#E07A2E 60%,#F6D49B)}
.add-photo{position:absolute;bottom:16px;width:100%;display:flex;justify-content:center;align-items:center;gap:5px;font-size:7px;font-weight:600;color:var(--orange-text)}
.grid{position:absolute;left:14px;right:14px;top:140px;display:grid;grid-template-columns:repeat(4,1fr);gap:8px}
.grid span{height:50px;border:1px solid var(--line);border-radius:4px;display:flex;align-items:center;justify-content:center;font-size:7px;font-weight:600;box-shadow:0 1px 3px rgba(0,0,0,.05)}
.panel{position:absolute;left:14px;right:14px;top:135px;background:var(--panel);border-radius:5px;padding:6px}
.item{height:22px;background:#fff;border-radius:3px;display:flex;align-items:center;padding:0 8px;font-size:6.5px;margin-bottom:5px}
.item span{flex:1}
.item svg{margin-left:8px}
.add-link{font-size:7px;line-height:10px;font-weight:600;color:var(--orange-text);display:flex;align-items:center;gap:5px;padding:4px 2px 14px}
.form{background:#fff;border:1px solid var(--orange);border-radius:4px;padding:6px;margin-bottom:2px}
.input{height:22px;border-bottom:1px solid var(--line);display:flex;align-items:center;justify-content:space-between;font-size:6px;color:#B5B5B5;padding:0 6px}
.inputs{display:flex;gap:6px;margin-top:8px}
.inputs div{flex:1;height:22px;border:1px solid var(--line);border-radius:3px;display:flex;align-items:center;justify-content:space-between;padding:0 7px;font-size:6px;color:#B5B5B5}
.inputs .select{color:var(--ink)}
.connectors{position:absolute;left:0;top:0;pointer-events:none}
</style>
</head>
<body>

<svg width="0" height="0" style="position:absolute">
  <defs>
    <symbol id="ic-close" viewBox="0 0 10 10"><path d="M1 1l8 8M9 1L1 9" stroke="currentColor" stroke-width="1.3"/></symbol>
    <symbol id="ic-save" viewBox="0 0 10 10"><rect x="0.5" y="0.5" width="9" height="9" rx="1.3" fill="currentColor"/><rect x="2.3" y="1.3" width="5" height="2.6" fill="#E98D56"/><circle cx="5" cy="6.6" r="1.3" fill="#E98D56"/></symbol>
    <symbol id="ic-arrow-r" viewBox="0 0 10 10"><path d="M1 5h8M5.5 1.5L9 5 5.5 8.5" fill="none" stroke="currentColor" stroke-width="1.2"/></symbol>
    <symbol id="ic-arrow-l" viewBox="0 0 10 10"><path d="M9 5H1M4.5 1.5L1 5l3.5 3.5" fill="none" stroke="currentColor" stroke-width="1.2"/></symbol>
    <symbol id="ic-pen" viewBox="0 0 10 10"><path d="M1.5 8.5l1-3 4.5-4.5 2 2-4.5 4.5z" fill="currentColor"/></symbol>
    <symbol id="ic-bin" viewBox="0 0 10 10"><rect x="2.5" y="3" width="5" height="6" rx=".6" fill="currentColor"/><rect x="1.8" y="1.5" width="6.4" height="1" fill="currentColor"/></symbol>
    <symbol id="ic-drag" viewBox="0 0 10 10" fill="#C8C8C8"><circle cx="3.5" cy="2" r=".8"/><circle cx="6.5" cy="2" r=".8"/><circle cx="3.5" cy="5" r=".8"/><circle cx="6.5" cy="5" r=".8"/><circle cx="3.5" cy="8" r=".8"/><circle cx="6.5" cy="8" r=".8"/></symbol>
    <symbol id="ic-image" viewBox="0 0 10 10"><rect x="0.5" y="0.5" width="9" height="9" rx="1.2" fill="currentColor"/><path d="M2 8l2.5-3 2 2 1-1L8.5 8z" fill="#fff"/></symbol>
    <symbol id="ic-status" viewBox="0 0 40 10" fill="#fff"><rect x="0" y="6" width="2" height="3"/><rect x="3" y="4.5" width="2" height="4.5"/><rect x="6" y="3" width="2" height="6"/><rect x="9" y="1.5" width="2" height="7.5"/><path d="M14 4a7 7 0 0 1 9 0l-1.2 1.3a5 5 0 0 0-6.6 0zM16.3 6.4a3.6 3.6 0 0 1 4.4 0L18.5 9z"/><rect x="26" y="1.5" width="13" height="7" rx="2"/></symbol>
    <symbol id="ring" viewBox="0 0 54 54"><circle cx="27" cy="27" r="25" fill="#fff"/><circle cx="27" cy="27" r="23.5" fill="none" stroke="#E2E2E2" stroke-width="3"/></symbol>
  </defs>
</svg>

<!-- Step 1 -->
<div class="flow-label" style="left:40px;top:28px;height:260px">NEW RECIPE - STEP 1</div>
<section class="screen" style="left:72px;top:28px">
  <div class="header">
    <div class="status"><span>9:41</span><svg width="26" height="7"><use href="#ic-status"/></svg></div>
    <div class="titlebar"><svg width="9" height="9"><use href="#ic-close"/></svg><h1>Add new Recipe</h1><svg width="10" height="10" style="color:#fff"><use href="#ic-save"/></svg></div>
  </div>
  <div class="body">
    <svg class="step-badge" viewBox="0 0 54 54"><use href="#ring"/><path d="M27 3.5A23.5 23.5 0 0 1 50.3 30" fill="none" stroke="#E98D56" stroke-width="3"/><path d="M17 30h20v3H17zM19 29a8 8 0 0 1 16 0z" fill="#1AA899"/><rect x="24" y="19" width="6" height="2" rx="1" fill="#1AA899"/></svg>
    <div class="step-meta"><small>STEP 1 OF 4</small><strong>Recipe Name and Photo</strong></div>
    <div class="name-field">Recipe name <svg width="8" height="8" style="color:var(--orange-text)"><use href="#ic-pen"/></svg></div>
    <div class="label" style="top:152px">Photo of your recipe</div>
    <div class="photo-box">
      <div class="illustration" role="img" aria-label="Illustration of a cooking pot with a cutting board and ingredients"></div>
      <div class="add-photo"><svg width="7" height="7"><use href="#ic-image"/></svg>Add a photo</div>
    </div>
    <div class="footer">
      <div class="progress-row"><span>PROGRESS</span><span>14.4%</span></div>
      <div class="bar"><i style="width:16%"></i></div>
      <div class="buttons"><div class="btn btn-next">Next <svg width="8" height="8"><use href="#ic-arrow-r"/></svg></div></div>
    </div>
  </div>
  <div class="home"></div>
</section>

<!-- Step 2 -->
<div class="flow-label" style="left:348px;top:28px;height:260px">NEW RECIPE - STEP 2</div>
<section class="screen" style="left:380px;top:28px">
  <div class="header">
    <div class="status"><span>9:41</span><svg width="26" height="7"><use href="#ic-status"/></svg></div>
    <div class="titlebar"><svg width="9" height="9"><use href="#ic-close"/></svg><h1>Add new Recipe</h1><svg width="10" height="10" style="color:#fff"><use href="#ic-save"/></svg></div>
  </div>
  <div class="body">
    <svg class="step-badge" viewBox="0 0 54 54"><use href="#ring"/><path d="M27 3.5A23.5 23.5 0 0 1 40 46.5" fill="none" stroke="#E98D56" stroke-width="3"/><g fill="#1AA899"><circle cx="23" cy="23" r="4"/><circle cx="32" cy="23" r="3.5"/><path d="M15 34a8 6 0 0 1 16 0zM29 34a6 5 0 0 1 11 0z"/></g></svg>
    <div class="step-meta"><small>STEP 2 OF 4</small><strong>Servings</strong></div>
    <div class="label" style="top:120px">Good for how many persons?</div>
    <div class="grid"><span>1</span><span>2</span><span>3</span><span>4</span><span>5</span><span>6</span><span>7</span><span>8</span><span>9</span><span>10</span><span>10-15</span><span>15-20</span></div>
    <div class="footer">
      <div class="progress-row"><span>PROGRESS</span><span>40.2%</span></div>
      <div class="bar"><i style="width:36%"></i></div>
      <div class="buttons"><div class="btn btn-prev"><svg width="8" height="8"><use href="#ic-arrow-l"/></svg> Prev</div><div class="btn btn-next">Next <svg width="8" height="8"><use href="#ic-arrow-r"/></svg></div></div>
    </div>
  </div>
  <div class="home"></div>
</section>

<!-- Step 3 -->
<div class="flow-label" style="left:40px;top:640px;height:260px">NEW RECIPE - STEP 3</div>
<section class="screen" style="left:72px;top:640px">
  <div class="header">
    <div class="status"><span>9:41</span><svg width="26" height="7"><use href="#ic-status"/></svg></div>
    <div class="titlebar"><svg width="9" height="9"><use href="#ic-close"/></svg><h1>Add new Recipe</h1><svg width="10" height="10" style="color:#fff"><use href="#ic-save"/></svg></div>
  </div>
  <div class="body">
    <svg class="step-badge" viewBox="0 0 54 54"><use href="#ring"/><path d="M27 3.5A23.5 23.5 0 1 1 8 41" fill="none" stroke="#E98D56" stroke-width="3"/><g fill="#1AA899"><rect x="23" y="15" width="8" height="4" rx="1"/><path d="M22 21h10l1 4v12a2 2 0 0 1-2 2h-8a2 2 0 0 1-2-2V25z"/></g><rect x="24" y="28" width="6" height="6" fill="#fff"/></svg>
    <div class="step-meta"><small>STEP 3 OF 4</small><strong>Ingredients</strong></div>
    <div class="label" style="top:118px">List of ingredients</div>
    <div class="panel">
      <div class="item"><span>250 mL milk</span><svg width="7" height="7" style="color:var(--teal)"><use href="#ic-pen"/></svg><svg width="7" height="7" style="color:var(--red)"><use href="#ic-bin"/></svg><svg width="7" height="7"><use href="#ic-drag"/></svg></div>
      <div class="item"><span>10 grams chocolate</span><svg width="7" height="7" style="color:var(--teal)"><use href="#ic-pen"/></svg><svg width="7" height="7" style="color:var(--red)"><use href="#ic-bin"/></svg><svg width="7" height="7"><use href="#ic-drag"/></svg></div>
      <div class="add-link"><svg width="8" height="8" viewBox="0 0 10 10"><circle cx="5" cy="5" r="5" fill="#E06B2A"/><path d="M5 2.5v5M2.5 5h5" stroke="#fff" stroke-width="1.3"/></svg>Add ingredient</div>
    </div>
    <div class="footer">
      <div class="progress-row"><span>PROGRESS</span><span>54.8 %</span></div>
      <div class="bar"><i style="width:58%"></i></div>
      <div class="buttons"><div class="btn btn-prev"><svg width="8" height="8"><use href="#ic-arrow-l"/></svg> Prev</div><div class="btn btn-next">Next <svg width="8" height="8"><use href="#ic-arrow-r"/></svg></div></div>
    </div>
  </div>
  <div class="home"></div>
</section>

<!-- Step 3 with form -->
<div class="flow-label" style="left:348px;top:640px;height:260px">NEW RECIPE - STEP 3</div>
<section class="screen" style="left:380px;top:640px">
  <div class="header">
    <div class="status"><span>9:41</span><svg width="26" height="7"><use href="#ic-status"/></svg></div>
    <div class="titlebar"><svg width="9" height="9"><use href="#ic-close"/></svg><h1>Add new Recipe</h1><svg width="10" height="10" style="color:#fff"><use href="#ic-save"/></svg></div>
  </div>
  <div class="body">
    <svg class="step-badge" viewBox="0 0 54 54"><use href="#ring"/><path d="M27 3.5A23.5 23.5 0 1 1 8 41" fill="none" stroke="#E98D56" stroke-width="3"/><g fill="#1AA899"><rect x="23" y="15" width="8" height="4" rx="1"/><path d="M22 21h10l1 4v12a2 2 0 0 1-2 2h-8a2 2 0 0 1-2-2V25z"/></g><rect x="24" y="28" width="6" height="6" fill="#fff"/></svg>
    <div class="step-meta"><small>STEP 3 OF 4</small><strong>Ingredients</strong></div>
    <div class="label" style="top:118px">List of ingredients</div>
    <div class="panel">
      <div class="item"><span>250 mL milk</span><svg width="7" height="7" style="color:var(--teal)"><use href="#ic-pen"/></svg><svg width="7" height="7" style="color:var(--red)"><use href="#ic-bin"/></svg><svg width="7" height="7"><use href="#ic-drag"/></svg></div>
      <div class="item"><span>10 grams chocolate</span><svg width="7" height="7" style="color:var(--teal)"><use href="#ic-pen"/></svg><svg width="7" height="7" style="color:var(--red)"><use href="#ic-bin"/></svg><svg width="7" height="7"><use href="#ic-drag"/></svg></div>
      <div class="form">
        <div class="input"><span>Item name</span><svg width="6" height="6" style="color:var(--ink)"><use href="#ic-close"/></svg></div>
        <div class="inputs"><div>Quantity</div><div class="select">Select <svg width="6" height="4" viewBox="0 0 6 4"><path d="M0 0h6L3 4z" fill="#2E2E2E"/></svg></div></div>
      </div>
    </div>
    <div class="footer">
      <div class="progress-row"><span>PROGRESS</span><span>54.8 %</span></div>
      <div class="bar"><i style="width:58%"></i></div>
      <div class="buttons"><div class="btn btn-prev"><svg width="8" height="8"><use href="#ic-arrow-l"/></svg> Prev</div><div class="btn btn-next">Next <svg width="8" height="8"><use href="#ic-arrow-r"/></svg></div></div>
    </div>
  </div>
  <div class="home"></div>
</section>

<svg class="connectors" width="682" height="1200" viewBox="0 0 682 1200" fill="none" stroke="#1A9E96" stroke-width="1">
  <circle cx="300" cy="525" r="2.5" fill="#1A9E96"/>
  <path d="M300 525V592H428V576"/>
  <path d="M424 580l4-5 4 5"/>
  <circle cx="162" cy="961" r="2.5" fill="#1A9E96"/>
  <path d="M162 961V1000H370"/>
  <path d="M365 996l5 4-5 4"/>
</svg>

</body>
</html>
```